MO&A - Business Card and Stationery for a Law Firm
Mendívil Ortuzar & Asociados
Professional
Julián Esteban Mendívil Ortuzar
Abogado
Carrera 48 No. 62-14 Of. 305
Bogotá D.C., Colombia
julian.mendivil@mendivilortuzar.com
www.mendivilortuzar.com
The text on the back of the card is in Spanish, for your information the meaning in English is as follows:
Companies in Colombia and abroad.
International business.
Tax planning.
Foreign investments.
Inmigration.
Industrial property.
Please distribute the text as you consider.
Logo and the following text:
Sociedades en Colombia y el exterior.
Negocios internacionales.
Planeación tributaria.
Inversión extranjera.
Asuntos migratorios.
Propiedad Industrial.

```html
<!DOCTYPE html>
<html lang="es">
<head>
<meta charset="utf-8">
<title>MO&amp;A – Tarjetas de presentación</title>
<link rel="stylesheet" href="https://fonts.googleapis.com/css2?family=Cinzel:wght@400;600&display=swap">
<style>
  :root{
    --navy:#1b2a4e;
    --navy-soft:#2a3a61;
    --frame:#0f1c3d;
    --stage:#e2e4e8;
    --white:#ffffff;
    --grey-card:#9a9ea6;
    --grey-line:#b9bcc3;
    --ink:#2b2f3a;
    --faint-on-navy:rgba(255,255,255,0.10);
    --faint-on-white:rgba(27,42,78,0.07);
  }
  *{margin:0;padding:0;box-sizing:border-box}
  html,body{width:1200px;height:726px;overflow:hidden;background:var(--frame)}
  .stage{
    position:absolute;left:14px;top:14px;width:1172px;height:698px;
    background:linear-gradient(180deg,#eceef1 0%,var(--stage) 100%);
    font-family:"Cinzel",serif;
  }
  .card{
    position:absolute;width:512px;height:290px;border-radius:16px;overflow:hidden;
    box-shadow:0 2px 6px rgba(0,0,0,0.25);
  }
  .card--front{left:53px;top:53px;background:var(--white)}
  .card--back-navy{left:584px;top:53px;background:var(--navy)}
  .card--back-white{left:53px;top:360px;background:var(--white)}
  .card--back-grey{left:584px;top:360px;background:var(--grey-card)}

  .mark{display:flex;align-items:center;gap:8px;position:absolute}
  .mark__square{width:26px;height:26px;background:var(--navy)}
  .mark__name{font-weight:600;font-size:26px;letter-spacing:1px;color:var(--navy);line-height:1}
  .on-navy .mark__square{background:var(--white)}
  .on-navy .mark__name{color:var(--white)}

  /* front */
  .card--front .mark{left:22px;top:22px}
  .firm-name{position:absolute;left:168px;top:20px;color:var(--navy);font-size:19px;line-height:22px;letter-spacing:.5px}
  .person{position:absolute;left:0;right:0;top:108px;text-align:center;color:var(--navy)}
  .person__name{font-size:19px;letter-spacing:.5px}
  .person__role{font-size:12px;margin-top:6px;color:var(--ink)}
  .contact{position:absolute;left:22px;top:168px;font-size:11px;line-height:14.5px;color:var(--ink);letter-spacing:.2px}
  .swoosh{position:absolute;left:0;bottom:0;width:512px;height:110px}

  /* backs */
  .services{font-size:15.5px;line-height:18px;letter-spacing:.3px}
  .card--back-navy .mark{left:50px;top:44px}
  .card--back-navy .services{position:absolute;left:20px;top:160px;color:var(--white)}
  .card--back-white .mark,.card--back-grey .mark{left:50%;transform:translateX(-50%);top:64px}
  .card--back-white .services,.card--back-grey .services{position:absolute;left:0;right:0;top:152px;text-align:center;color:var(--navy)}
  .faint-block{position:absolute}
  .card--back-navy .faint-block{right:36px;top:34px;width:160px;height:200px;background:var(--faint-on-navy)}
  .card--back-white .faint-block{right:58px;top:40px;width:150px;height:150px;background:var(--faint-on-white)}
</style>
</head>
<body>
<main class="stage">

  <section class="card card--front" aria-label="Frente de la tarjeta">
    <div class="mark"><span class="mark__square"></span><span class="mark__name">MO&amp;A</span></div>
    <div class="firm-name">Mendívil Ortuzar<br>&amp; Asociados</div>
    <div class="person">
      <div class="person__name">Julián Esteban Mendívil Ortuzar</div>
      <div class="person__role">Abogado</div>
    </div>
    <div class="contact">
      Carrera 48 No. 62-14 Of. 305<br>
      Bogotá D.C., Colombia<br>
      Cel.: +57 3005550142 | Phone: +57 (1) 5550187<br>
      Email: julian.mendivil@mendivilortuzar.com<br>
      www.mendivilortuzar.com
    </div>
    <svg class="swoosh" viewBox="0 0 512 110" preserveAspectRatio="none" aria-hidden="true">
      <path d="M300 110 C360 70 420 30 512 20 L512 110 Z" fill="var(--grey-line)"/>
      <path d="M0 92 C150 100 290 95 380 60 C430 40 470 38 512 52 L512 110 L0 110 Z" fill="var(--navy)"/>
      <path d="M380 60 C430 40 470 38 512 52 L512 44 C470 30 425 34 380 60 Z" fill="var(--white)"/>
    </svg>
  </section>

  <section class="card card--back-navy on-navy" aria-label="Reverso azul">
    <div class="faint-block"></div>
    <div class="mark"><span class="mark__square"></span><span class="mark__name">MO&amp;A</span></div>
    <p class="services">
      Sociedades en Colombia y el exterior.<br>
      Negocios internacionales.<br>
      Planeación tributaria.<br>
      Inversión extranjera.<br>
      Asuntos migratorios.<br>
      Propiedad Industrial.
    </p>
  </section>

  <section class="card card--back-white" aria-label="Reverso blanco">
    <div class="faint-block"></div>
    <div class="mark"><span class="mark__square"></span><span class="mark__name">MO&amp;A</span></div>
    <p class="services">
      Sociedades en Colombia y el exterior.<br>
      Negocios internacionales.<br>
      Planeación tributaria.<br>
      Inversión extranjera.<br>
      Asuntos migratorios.<br>
      Propiedad Industrial.
    </p>
  </section>

  <section class="card card--back-grey" aria-label="Reverso gris">
    <div class="mark"><span class="mark__square"></span><span class="mark__name">MO&amp;A</span></div>
    <p class="services">
      Sociedades en Colombia y el exterior.<br>
      Negocios internacionales.<br>
      Planeación tributaria.<br>
      Inversión extranjera.<br>
      Asuntos migratorios.<br>
      Propiedad Industrial.
    </p>
  </section>

</main>
</body>
</html>
```